Dozing Heron

Need a business card for our restaurant. Restaurant and Bar in the mountains of North Idaho. Rustic looking card

Contact Information for Business Card

rustic design, wood and metal looking, primarily neutral colors

Requirements
Must have
• Name, address, phone number, website, email address

```html
<!DOCTYPE html>
<html lang="en">
<head>
<meta charset="utf-8">
<title>Dozing Heron – Business Card</title>
<link href="https://fonts.googleapis.com/css2?family=Lato:wght@400;700&display=swap" rel="stylesheet">
<style>
  :root {
    --stage: #6b6b6b;
    --card-dark: #141414;
    --pattern-dark: #1f1f1f;
    --pattern-light: #3a3a3a;
    --card-light: #ffffff;
    --ink: #1a1a1a;
    --ink-soft: #3c3c3c;
    --rule: #4a4a4a;
  }
  * { box-sizing: border-box; margin: 0; padding: 0; }
  html, body { width: 1200px; height: 900px; overflow: hidden; }
  body {
    background: var(--stage);
    font-family: "Lato", sans-serif;
    position: relative;
  }
  .card {
    position: absolute;
    width: 640px;
    height: 380px;
    border-radius: 26px;
    box-shadow: 0 18px 40px rgba(0,0,0,0.35);
    overflow: hidden;
  }
  .card-back {
    left: 80px;
    top: 90px;
    background: var(--card-dark);
  }
  .card-back .pattern {
    position: absolute;
    inset: 0;
    background: radial-gradient(circle at 60% 20%, var(--pattern-light), var(--pattern-dark) 55%, var(--card-dark));
  }
  .card-back .brand-name {
    position: absolute;
    left: 0; right: 0;
    top: 50%;
    transform: translateY(-50%);
    text-align: center;
    color: #ffffff;
    font-weight: 700;
    font-size: 26px;
    letter-spacing: 1px;
  }
  .card-front {
    left: 480px;
    top: 400px;
    background: var(--card-light);
    color: var(--ink);
  }
  .brand-mark {
    position: absolute;
    top: 28px;
    right: 40px;
    width: 140px;
    height: 140px;
    border: 3px solid var(--ink);
    border-radius: 50%;
    display: flex;
    align-items: center;
    justify-content: center;
    text-align: center;
    font-weight: 700;
    font-size: 20px;
    line-height: 1.2;
    color: var(--ink);
  }
  .divider-main {
    position: absolute;
    left: 40px;
    right: 40px;
    top: 186px;
    border-top: 1.5px solid var(--rule);
  }
  .person {
    position: absolute;
    left: 40px;
    top: 200px;
  }
  .person-name {
    font-weight: 700;
    font-size: 27px;
    line-height: 1.2;
    color: var(--ink);
  }
  .person-role {
    font-size: 17px;
    color: var(--ink-soft);
    margin-top: 4px;
    padding-bottom: 8px;
    width: 230px;
    border-bottom: 1.5px solid var(--rule);
  }
  .contacts {
    list-style: none;
    margin-top: 8px;
  }
  .contacts li {
    display: flex;
    align-items: center;
    gap: 12px;
    font-size: 18px;
    color: var(--ink);
    line-height: 1.4;
  }
  .contacts svg { width: 16px; height: 16px; fill: var(--ink); flex: none; }
  .address {
    position: absolute;
    right: 40px;
    top: 214px;
    text-align: right;
    font-size: 19px;
    line-height: 1.35;
    color: var(--ink);
  }
</style>
</head>
<body>
  <section class="card card-back">
    <div class="pattern" role="img" aria-label="Tonal embossed repeating brand pattern"></div>
    <div class="brand-name">Dozing Heron</div>
  </section>

  <section class="card card-front">
    <div class="brand-mark">Dozing<br>Heron</div>
    <div class="divider-main"></div>

    <div class="person">
      <div class="person-name">Daniel Hart</div>
      <div class="person-role">Owner</div>
      <ul class="contacts">
        <li>
          <svg viewBox="0 0 16 16"><path d="M3.5 1.5l2.5 0 1 3.5-1.8 1.2a8 8 0 0 0 4.6 4.6L11 9l3.5 1v2.5a2 2 0 0 1-2 2A11 11 0 0 1 1.5 3.5a2 2 0 0 1 2-2z"/></svg>
          123.456.7890
        </li>
        <li>
          <svg viewBox="0 0 16 16"><path d="M1 3h14v10H1z M1.5 3.5L8 8.5l6.5-5" fill="none" stroke="#1a1a1a" stroke-width="1.5"/><path d="M1 3h14L8 8.5z"/></svg>
          info@webname.com
        </li>
        <li>
          <svg viewBox="0 0 16 16"><circle cx="8" cy="8" r="7"/><path d="M5 4c2 1 1 3 3 3s1 3-1 4M10 3c0 2 2 2 3 3" stroke="#fff" stroke-width="1.2" fill="none"/></svg>
          www.website.com
        </li>
      </ul>
    </div>

    <div class="address">
      421, Address line goes here<br>
      45452, Country name
    </div>
  </section>
</body>
</html>
```